GFA at Haldane's

I am looking to mail out a postacrd to GFA ehtusiasts that highlights our beer specials and our wings special during all televised GFA games. Games televised in HD on our 18 large screen TV's

Domestic Buckets Bottles 5 for $12.00 Import buckets 5 for $15 In bold .35 cent wings with every Bucket purchased. small print (Minimum order 10 wings, must be ordered by 10's)

This promotion is to highlight the wings and Beer special

Target Market(s)

Male sports GFA enthusiasts 21-60 yrs old

Industry/Entity Type

Tv

Requirements
Must have
• Must highlight the special.
Must have Logo
Must have picture of weings beer buckets and funn crowd photos and interior shots.
Must have address of location and hours of operation;

Haldane's Tavern and Grill
2740 Millbrook Blvd., Suite 320
Boynton Beach Fl 33471
PH:561-482-6130
Email:hdtavern@mailvora.com
Web www.hdtavern-example.com
(Just east of Palmetto ave. in the Juniper Crossing plaza near Beanloft and The Grape Ledger)
Hours of operation
Sun-Thursday 11:30am - Midnight Fri - Sat 11;30am - 2:00am
LIVE MUSIC Thurs, fri, and sat Nights.

```html
<!DOCTYPE html>
<html lang="en">
<head>
<meta charset="utf-8">
<title>Haldane's Tavern and Grill – Bucket &amp; Wings Postcard</title>
<link rel="stylesheet" href="https://fonts.googleapis.com/css2?family=Arvo:wght@400;700&display=swap">
<style>
  :root {
    --stage: #e9e4e8;
    --card-white: #ffffff;
    --promo-red: #c4161c;
    --navy: #0f2250;
    --hours-yellow: #f4d53a;
    --gold-box: #b4a443;
    --ink: #1a1a2a;
    --promo-bg: #3a1c10;
    --beer-bucket: #5c6682;
    --import-bucket: #5f7f52;
    --guests: #8a6a52;
    --wings: #a84a1c;
    --crowd: #6e4628;
    --bartender: #7a5a3c;
  }
  * { box-sizing: border-box; margin: 0; padding: 0; }
  html, body {
    width: 1200px; height: 604px; overflow: hidden;
    background: var(--stage);
    font-family: "Arvo", Georgia, serif;
  }
  .postcard {
    position: absolute; left: 145px; top: 17px;
    width: 910px; height: 570px;
    background: var(--card-white);
    box-shadow: 0 4px 18px rgba(0,0,0,.18);
    display: grid;
    grid-template-rows: 187px 186px 135px 62px;
  }
  .photo-row { display: grid; }
  .photo-row--top { grid-template-columns: 197px 545px 168px; }
  .photo-row--middle { grid-template-columns: 197px 372px 173px 168px; }
  .photo { width: 100%; height: 100%; }
  .photo--beer-bucket { background: var(--beer-bucket); }
  .photo--import-bucket { background: var(--import-bucket); }
  .photo--guests { background: var(--guests); }
  .photo--wings-plate { background: var(--wings); }
  .photo--crowd { background: var(--crowd); }
  .photo--bartender { background: var(--bartender); }
  .promo {
    background: var(--promo-bg);
    display: flex; flex-direction: column; align-items: center; justify-content: center;
  }
  .promo__headline {
    background: var(--promo-red);
    color: #fff;
    font-weight: 700; font-size: 24.5px; line-height: 1.18;
    text-align: center;
    padding: 6px 14px 8px;
    border-radius: 10px;
  }
  .promo__fineprint { color: #fff; font-size: 9px; margin-top: 12px; }
  .contact {
    display: grid;
    grid-template-columns: 197px 466px 247px;
  }
  .brand {
    display: flex; align-items: center; justify-content: center; gap: 7px;
    color: var(--promo-red); font-weight: 700; font-size: 18px;
  }
  .brand__dot { width: 12px; height: 12px; border-radius: 50%; background: var(--promo-red); flex: none; }
  .contact__list {
    list-style: none; padding: 16px 0 0 6px;
    font-weight: 700; font-size: 15.5px; color: var(--ink);
  }
  .contact__list li { display: flex; align-items: center; gap: 8px; height: 25px; white-space: nowrap; }
  .contact__list svg { width: 13px; height: 13px; flex: none; }
  .directions {
    background: var(--gold-box);
    color: var(--ink); font-size: 14.5px; line-height: 1.3;
    text-align: center;
    padding: 22px 10px 0;
  }
  .hours {
    background: var(--navy); color: var(--hours-yellow);
    font-weight: 700; font-size: 15.5px; text-align: center;
    display: flex; flex-direction: column; justify-content: center; line-height: 1.4;
  }
</style>
</head>
<body>
  <article class="postcard">
    <section class="photo-row photo-row--top">
      <div class="photo photo--beer-bucket" role="img" aria-label="Bucket of domestic beer bottles on ice"></div>
      <div class="promo">
        <h1 class="promo__headline">Domestic Buckets Bottles 5 for $12.00,<br>Import buckets 5 for $15<br>In bold .35 cent wings with<br>every Bucket purchased.</h1>
        <p class="promo__fineprint">(Minimum order 10 wings, must be ordered by 10's)</p>
      </div>
      <div class="photo photo--import-bucket" role="img" aria-label="Bucket of import beer bottles on ice"></div>
    </section>
    <section class="photo-row photo-row--middle">
      <div class="photo photo--guests" role="img" aria-label="Guests enjoying drinks together inside the tavern"></div>
      <div class="photo photo--wings-plate" role="img" aria-label="Plate of chicken wings with dipping sauce"></div>
      <div class="photo photo--crowd" role="img" aria-label="Lively crowd watching televised GFA games on the 18 large HD screens"></div>
      <div class="photo photo--bartender" role="img" aria-label="Bartender pouring draft beer at the taps"></div>
    </section>
    <section class="contact">
      <div class="brand"><span class="brand__dot"></span>Haldane's</div>
      <ul class="contact__list">
        <li><svg viewBox="0 0 12 12"><circle cx="6" cy="6" r="6" fill="#1a1a2a"/><path d="M6 2.5a2 2 0 0 0-2 2c0 1.6 2 4.5 2 4.5s2-2.9 2-4.5a2 2 0 0 0-2-2z" fill="#fff"/></svg>2740 Millbrook Blvd., Suite 320, Boynton Beach Fl 33471</li>
        <li><svg viewBox="0 0 12 12"><circle cx="6" cy="6" r="6" fill="#1a1a2a"/><path d="M4 3l1.2 1.4-.6.8a4 4 0 0 0 2.2 2.2l.8-.6L9 8l-.7.9C6 8.8 3.2 6 3.1 3.7z" fill="#fff"/></svg>561-482-6130</li>
        <li><svg viewBox="0 0 12 12"><circle cx="6" cy="6" r="6" fill="#1a1a2a"/><rect x="3" y="4" width="6" height="4.2" fill="none" stroke="#fff" stroke-width=".9"/><path d="M3 4l3 2.3L9 4" fill="none" stroke="#fff" stroke-width=".9"/></svg>hdtavern@mailvora.com</li>
        <li><svg viewBox="0 0 12 12"><circle cx="6" cy="6" r="6" fill="#1a1a2a"/><circle cx="6" cy="6" r="3" fill="none" stroke="#fff" stroke-width=".8"/><path d="M3 6h6M6 3v6" stroke="#fff" stroke-width=".7"/></svg>www.hdtavern-example.com</li>
      </ul>
      <p class="directions">(Just east of Palmetto ave.<br>in the Juniper Crossing<br>plaza near Beanloft and<br>The Grape Ledger)</p>
    </section>
    <footer class="hours">
      <p>HOURS OF OPERATION: Sun-Thursday 11:30am - Midnight Fri - Sat 11;30am - 2:00am</p>
      <p>LIVE MUSIC: Thurs, fri, and sat Nights.</p>
    </footer>
  </article>
</body>
</html>
```